Webdesign for large cottage directory

We have developed a first version of a website that can accommodate large groups (10 to 300 people). The site is English and is aimed at a wide audience ranging from a group of students to a family or a family. For the visitors the site is free and it is the propietaires who pay to see their accommodation. The site is online with just a few fake lodgings and a simple design to the elements that must be appraised (nothing to keep the current design). Our website is here: lodgevista.com (login / pass = admin / 123) Home page (lodgevista.com): on this page section) and lodging by theme (third section). These three points should be highlighted as possible. The displayed map may be slightly modified. Only the background and the color changes when hovering over the mouse. It can be enlarged / retreciated. Below these 3 sections we have some fairly published articles, the latest blog posts and the footer. The menu will be visible throughout the site. Category page (https://lodgevista.fr/gite-departement/aveyron OR https://lodgevista.fr/gites-couchages-121): On these pages we always return the same format with the googlemap, an image 1 text. Below the list of the cottages concerned and the filter options. Product page: The pages presenting the cottages can be of two types: - Either the cottage has no owner and there is no contact for the visitor to the owner that he can retrieve his cottage by registering: example of a page of this type: https://lodgevista.fr/domaine-de-fressanac - The cottage to a propietaire and we are on the classic card. : // lodgevista. en / domain-of-fressanac2 For all products on the site we have nav tab. It's just for testing. We do not want to be in the design for real website. All information must be in the page without login / register page: classic, it's here: https://lodgevista.it/login and https://lodgevista.fr/register Blog homepage (https://lodgevista.fr/blog ): Classic blog page Blog post (https://lodgevista.fr/blog/urltemporaire1551521154) and static page (https://lodgevista.fr/blog/Systeme-classement-lodgevistafr): Nothing special Menu: Menu is an important part of the website. It's the way to navigate on the wbesite.
Faible participation designers
Number of Pages Required
4 page
Colors
Designer to choose colors to be used in the design.
Look and feel
Each slider illustrates characteristics of the customer's brand and the style your logo design should communicate.

```html
<!DOCTYPE html>
<html lang="en">
<head>
<meta charset="utf-8">
<title>LodgeVista – Large Group Cottages</title>
<link rel="stylesheet" href="https://fonts.googleapis.com/css2?family=Dosis:wght@400;500;600;700&display=swap">
<style>
:root{
  --blue:#1a82d6;
  --blue-dark:#1468ad;
  --ink:#3f3f3f;
  --grey-text:#6b6b6b;
  --light-bg:#ebebeb;
  --card-bg:#e6e6e6;
  --footer:#4b4b4b;
  --white:#ffffff;
}
*{box-sizing:border-box;margin:0;padding:0}
html,body{width:1200px;height:3684px;overflow:hidden}
body{font-family:'Dosis',sans-serif;color:var(--ink);background:var(--white);position:relative}

/* header */
.hero{position:absolute;left:0;top:0;width:1200px;height:627px;
  background:linear-gradient(180deg,#3f8fd6 0%,#6aaee4 16%,#5f8f3e 34%,#4a7430 58%,#6f9c45 80%,#7f9a58 100%)}
.main-nav{position:absolute;left:0;top:0;width:1200px;height:62px;background:rgba(26,130,214,.72);
  display:flex;align-items:center;padding:0 98px}
.main-nav a{color:var(--white);text-decoration:none;font-size:15px;font-weight:500;text-transform:uppercase;margin-right:62px;letter-spacing:.3px}
.owners-btn{margin-left:auto;margin-right:0!important;background:var(--white);color:var(--blue)!important;
  font-weight:700!important;padding:10px 22px;font-size:14px!important}

/* capacity + theme */
.section-title{font-size:37px;font-weight:500;text-transform:uppercase;letter-spacing:.5px;text-align:center;color:var(--ink)}
.section-title.blue{color:var(--blue)}
.browse{position:absolute;top:627px;left:0;width:1200px;height:652px}
.browse .col-title{position:absolute;top:52px}
.tile{position:absolute;height:61px;display:flex;align-items:center;justify-content:center;
  color:var(--white);font-size:30px;font-weight:500;text-transform:uppercase;line-height:1;text-align:center;
  text-shadow:0 1px 2px rgba(0,0,0,.5)}
.tile.active{background:linear-gradient(90deg,#1a6fbf,#3a95dd,#1a6fbf)}
.tile.two-line{font-size:27px;line-height:.95}
.t-stone{background:linear-gradient(90deg,#5a5048,#8a7a66,#4f463e)}
.t-dusk{background:linear-gradient(90deg,#3b3a4a,#6a5a54,#2f2f3d)}
.t-night{background:linear-gradient(90deg,#4a4f63,#6b6f84,#3c4054)}
.t-green{background:linear-gradient(90deg,#3f4a32,#6d6048,#354028)}
.t-castle{background:linear-gradient(90deg,#7a7f8c,#a7a49a,#6f7584)}
.t-grey{background:#555555}
.t-brown{background:linear-gradient(90deg,#6a4e35,#8b6a48,#5a4130)}
.t-slate{background:linear-gradient(90deg,#2e3a52,#55617a,#2a3448)}
.t-olive{background:linear-gradient(90deg,#535a3e,#7b7556,#4a4f36)}

/* location */
.location{position:absolute;top:1279px;left:0;width:1200px;height:806px;background:var(--light-bg)}
.location .section-title{position:absolute;top:52px;width:100%}
.map{position:absolute;left:98px;top:155px;width:492px;height:587px;
  background:radial-gradient(circle at 44% 42%,#c9def2 0%,#f4f6f8 30%,#f4f6f8 100%)}
.region-map{position:absolute;left:720px;top:312px;width:190px;height:216px;background:var(--blue)}
.region-name{position:absolute;left:712px;top:550px;font-size:37px;font-weight:500;text-transform:uppercase}

/* recent */
.recent{position:absolute;top:2085px;left:0;width:1200px;height:630px}
.recent .section-title{position:absolute;top:52px;width:100%}
.cottage-card{position:absolute;left:98px;top:153px;width:1001px;height:408px;background:var(--card-bg);display:flex}
.cottage-photo{width:502px;height:408px;background:linear-gradient(180deg,#6fb4e6 0%,#8fa3ae 30%,#6d6a62 55%,#7b8d55 75%,#c27a8a 100%)}
.cottage-info{padding:24px 0 0 34px}
.cottage-name{font-size:40px;font-weight:500;color:var(--blue);text-transform:uppercase;margin-bottom:26px}
.field{font-size:18px;text-transform:uppercase;color:var(--ink);height:45px}
.actions{display:flex;gap:14px;margin-top:12px}
.btn{display:inline-flex;align-items:center;justify-content:center;font-size:14px;font-weight:700;text-transform:uppercase;
  height:36px;padding:0 16px;border:2px solid var(--blue);color:var(--blue);background:var(--white);text-decoration:none}
.btn.solid{background:var(--blue);color:var(--white)}
.arrow{position:absolute;top:2394px;width:52px;height:100px}

/* blog */
.blog{position:absolute;top:2715px;left:0;width:1200px;height:718px;background:var(--light-bg)}
.blog .section-title{position:absolute;top:52px;width:100%}
.post{position:absolute;top:152px;width:313px;height:403px;background:var(--white)}
.post-photo{height:187px;background:linear-gradient(180deg,#3b3f52 0%,#5b4a3a 45%,#d8a048 70%,#8a5a2a 100%)}
.post-body{padding:14px 12px}
.post-title{font-size:19px;font-weight:500;color:var(--blue);text-transform:uppercase}
.post-date{font-size:11px;color:var(--grey-text);text-transform:uppercase;margin:12px 0 8px}
.post-text{font-size:11px;line-height:1.4;color:var(--grey-text)}
.post .btn{margin-top:16px;height:36px;font-size:12px;padding:0 16px}
.all-posts{position:absolute;top:619px;left:526px;width:148px;height:35px;font-size:12px}

/* footer */
.site-footer{position:absolute;top:3492px;left:0;width:1200px;height:130px;background:var(--footer);color:var(--white);text-align:center}
.footer-brand{font-size:30px;font-weight:700;text-transform:uppercase;padding-top:28px}
.footer-links{font-size:12px;font-weight:700;text-transform:uppercase;margin-top:14px}
.footer-links a{color:var(--white);text-decoration:none;margin:0 6px}
.copyright{position:absolute;top:3622px;left:0;width:1200px;height:62px;background:var(--blue);color:var(--white);
  font-size:11px;text-transform:uppercase;text-align:center;line-height:62px}
</style>
</head>
<body>

<header class="hero" role="img" aria-label="Photo of an old stone cottage on a green lawn with tall trees under a blue sky"></header>
<nav class="main-nav">
  <a href="#">Cottage by capacity</a>
  <a href="#">Cottage by location</a>
  <a href="#">Cottage by theme</a>
  <a href="#">Blog</a>
  <a href="#">Your favourites</a>
  <a href="#" class="owners-btn">Owners area</a>
</nav>

<section class="browse">
  <h2 class="section-title col-title" style="left:98px;width:485px">Cottage by capacity</h2>
  <h2 class="section-title col-title" style="left:617px;width:485px">Cottage by theme</h2>

  <a class="tile active" style="left:98px;top:153px;width:485px">2 - 20</a>
  <a class="tile t-stone" style="left:98px;top:228px;width:485px">20 - 40</a>
  <a class="tile t-dusk" style="left:98px;top:303px;width:485px">40 - 60</a>
  <a class="tile t-night" style="left:98px;top:378px;width:485px">60 - 80</a>
  <a class="tile t-green" style="left:98px;top:453px;width:485px">80 - 120</a>
  <a class="tile t-castle" style="left:98px;top:528px;width:485px">120 +</a>

  <a class="tile active" style="left:617px;top:153px;width:236px">Seminar</a>
  <a class="tile t-brown" style="left:868px;top:153px;width:234px">Fishing</a>
  <a class="tile t-olive" style="left:617px;top:228px;width:236px">Class themed</a>
  <a class="tile t-grey" style="left:868px;top:228px;width:234px">Coastal</a>
  <a class="tile t-brown" style="left:617px;top:303px;width:236px">Horse riding</a>
  <a class="tile t-slate two-line" style="left:868px;top:303px;width:234px">Snow, nature<br>&amp; hike</a>
  <a class="tile t-grey" style="left:617px;top:378px;width:236px">Seminar</a>
  <a class="tile t-olive" style="left:868px;top:378px;width:234px">Mountain biking</a>
  <a class="tile t-stone" style="left:617px;top:453px;width:236px">Gormet themed</a>
  <a class="tile t-grey" style="left:868px;top:453px;width:234px">Seminar</a>
  <a class="tile t-brown" style="left:617px;top:528px;width:236px">Summer camp</a>
  <a class="tile t-dusk two-line" style="left:868px;top:528px;width:234px">Integration<br>weekend</a>
</section>

<section class="location">
  <h2 class="section-title blue">Cottage by location</h2>
  <div class="map" role="img" aria-label="Outline map of France divided into regions, with one central region highlighted in blue"></div>
  <div class="region-map" role="img" aria-label="Enlarged map outline of the selected region in blue"></div>
  <p class="region-name">Region name</p>
</section>

<section class="recent">
  <h2 class="section-title">Recent cottages added</h2>
  <article class="cottage-card">
    <div class="cottage-photo" role="img" aria-label="Photo of a stone cottage with blue shutters and a flowering garden"></div>
    <div class="cottage-info">
      <h3 class="cottage-name">Cottage name</h3>
      <p class="field">Address:</p>
      <p class="field">Region:</p>
      <p class="field">Country:</p>
      <p class="field">Details:</p>
      <p class="field">Description:</p>
      <div class="actions">
        <a href="#" class="btn solid">Add to favourites</a>
        <a href="#" class="btn" style="width:150px">Read more</a>
      </div>
    </div>
  </article>
</section>
<svg class="arrow" style="left:14px" viewBox="0 0 52 100" aria-label="Previous"><polyline points="46,6 6,50 46,94" fill="none" stroke="#1a82d6" stroke-width="4"/></svg>
<svg class="arrow" style="left:1134px" viewBox="0 0 52 100" aria-label="Next"><polyline points="6,6 46,50 6,94" fill="none" stroke="#1a82d6" stroke-width="4"/></svg>

<section class="blog">
  <h2 class="section-title blue">Latest blog posts</h2>

  <article class="post" style="left:98px">
    <div class="post-photo" role="img" aria-label="Night photo of a lit glass pyramid before a palace"></div>
    <div class="post-body">
      <h3 class="post-title">Lorem ipsum</h3>
      <p class="post-date">Date:</p>
      <p class="post-text">Lorem ipsum dolor sit amet, consectetur adipiscing elit, sed do eiusmod tempor incididunt ut labore et dolore magna aliqua. Ut enim ad minim veniam, quis nostrud exercitation ullamco laboris nisi ut aliquip ex ea commodo consequat. Duis aute irure dolor in reprehenderit in voluptate velit esse cillum dolore eu fugiat nulla pariatur...</p>
      <a href="#" class="btn">Read more</a>
    </div>
  </article>

  <article class="post" style="left:443px">
    <div class="post-photo" role="img" aria-label="Night photo of a lit glass pyramid before a palace"></div>
    <div class="post-body">
      <h3 class="post-title">Lorem ipsum</h3>
      <p class="post-date">Date:</p>
      <p class="post-text">Lorem ipsum dolor sit amet, consectetur adipiscing elit, sed do eiusmod tempor incididunt ut labore et dolore magna aliqua. Ut enim ad minim veniam, quis nostrud exercitation ullamco laboris nisi ut aliquip ex ea commodo consequat. Duis aute irure dolor in reprehenderit in voluptate velit esse cillum dolore eu fugiat nulla pariatur...</p>
      <a href="#" class="btn">Read more</a>
    </div>
  </article>

  <article class="post" style="left:787px">
    <div class="post-photo" role="img" aria-label="Night photo of a lit glass pyramid before a palace"></div>
    <div class="post-body">
      <h3 class="post-title">Lorem ipsum</h3>
      <p class="post-date">Date:</p>
      <p class="post-text">Lorem ipsum dolor sit amet, consectetur adipiscing elit, sed do eiusmod tempor incididunt ut labore et dolore magna aliqua. Ut enim ad minim veniam, quis nostrud exercitation ullamco laboris nisi ut aliquip ex ea commodo consequat. Duis aute irure dolor in reprehenderit in voluptate velit esse cillum dolore eu fugiat nulla pariatur...</p>
      <a href="#" class="btn">Read more</a>
    </div>
  </article>

  <a href="#" class="btn solid all-posts">See all blog posts</a>
</section>

<footer class="site-footer">
  <p class="footer-brand">lodgevista.com</p>
  <p class="footer-links"><a href="#">Classification system</a><a href="#">General conditions</a></p>
</footer>
<p class="copyright">Copyright © 2019 LodgeVista. All rights reserved.</p>

</body>
</html>
```